New Consulting Firm News PowerPoint Template

We are a new consulting firm that specializes in Veltrix Unified Results Planning implementations in need of a new PowerPoint template. We need at least the following layouts:
• Main Cover Slide
• Agenda / Table of Contents
• Title slide for each of the agenda items leading into actual content
• Title + Content with nice bullets in the content
• Title + Sub-Title + Content with nice bullets in the content
• Title + Two Columns of Content
• Title + Sub-Title + Two Columns of Content
• Title + Three Columns of Content
• Title + Sub-Title + Three Columns of Content
• Title + Two Rows and Two Columns of Content (4 boxes)
• Title + Sub-Title + Two Rows and Two Columns of Content (4 boxes)
• Title + Blank
• Nascar Slide (Client logos arranged somehow)
• Case Study Slide
• Various infographic slides than can be used and modified would be amazing as well
Our logo has been uploaded and you can find our website here:
https://brankelladvisory.example
We would like the main theme colors to blend with our logo, but also have a variety of colors in the theme that compliment the main theme colors. Once we have selected a PowerPoint design we expect to immediately have a Word design contest and the winning PowerPoint design will likely be a heavy influence on the Word design.

Target Market(s)

CFO, CAO, VP of Finance, Controllers

Industry/Entity Type

Consulting

Font styles to use
Serif
Sans Serif

Requirements
Must have
• • Main Cover Slide
• Title + Blank
• Case Study Slide
Nice to have
• • Various infographic slides than can be used and modified would be amazing as well

```html
<!DOCTYPE html>
<html lang="en">
<head>
<meta charset="utf-8">
<title>Brankell Advisory – Slide Template Set</title>
<link href="https://fonts.googleapis.com/css2?family=Montserrat:wght@500;600;700&family=Lato:wght@400;700&display=swap" rel="stylesheet">
<style>
:root{
  --ink:#000;
  --paper:#f6f7f9;
  --white:#fff;
  --navy:#0b4797;
  --blue:#1660c0;
  --mid:#1d72d2;
  --sky:#2c86e2;
  --pale:#dfe6ef;
  --grey:#8b9099;
  --dark:#2d3540;
}
html,body{margin:0;width:1200px;height:1084px;overflow:hidden;background:var(--ink)}
.board{position:relative;width:1500px;height:1355px;transform:scale(.8);transform-origin:0 0;background:var(--ink)}
.slide{position:absolute;width:364px;height:257px;background:var(--paper);overflow:hidden;font-family:Lato,sans-serif}
.abs{position:absolute}
.s-title{position:absolute;left:6px;top:6px;margin:0;padding-left:4px;border-left:2px solid var(--blue);font:700 11px/13px Montserrat,sans-serif;color:var(--blue)}
.brand{position:absolute;right:8px;top:8px;display:flex;align-items:center;gap:3px;font:600 7.5px/9px Montserrat,sans-serif;letter-spacing:.4px;color:var(--blue)}
.brand i{width:7px;height:7px;background:var(--blue)}
.s-foot{position:absolute;left:0;right:0;bottom:0;height:7px;background:var(--blue);display:flex;justify-content:space-between;align-items:center;padding:0 4px;font:400 4.5px Lato,sans-serif;color:var(--white)}
.s-foot::after{content:"";position:absolute;left:318px;top:0;width:9px;height:7px;background:var(--paper);transform:skewX(-40deg)}
.on-blue .s-foot::after{background:var(--navy)}
.p{margin:0;font-size:5px;line-height:7.3px;color:var(--grey)}
.p.white{color:var(--white)}
.h{margin:0;font:700 6.5px/8px Montserrat,sans-serif;color:var(--blue)}
.h.mark::before{content:"";display:inline-block;width:6px;height:6px;margin-right:3px;background:var(--blue);vertical-align:-1px}
.photo{position:absolute}
.blue-bg{background:linear-gradient(135deg,var(--navy),var(--blue) 60%,var(--mid))}
.white-title{color:var(--white);border-color:var(--white)}
.col4{position:absolute;top:47px;height:172px;width:91px;padding:68px 7px 0;box-sizing:border-box;text-align:center}
.col4 svg{position:absolute;left:27px;top:14px}
.tbl-row{position:absolute;left:11px;width:342px;height:18px;display:flex;align-items:center}
.tbl-row b{width:48px;font:600 5px Montserrat,sans-serif;color:var(--blue);padding-left:18px}
.tbl-row .p{flex:1;font-size:4.6px;line-height:6px}
.axis{font:600 5.5px Montserrat,sans-serif;fill:var(--dark)}
.big-year{font:600 11px Montserrat,sans-serif;color:var(--blue)}
.pct{font:700 7px Montserrat,sans-serif;color:var(--blue)}
</style>
</head>
<body>
<main class="board">

<!-- Row 1 -->
<section class="slide blue-bg" style="left:11px;top:11px">
  <div class="abs" style="left:0;right:0;top:120px;display:flex;justify-content:center;align-items:center;gap:5px;font:600 13px Montserrat,sans-serif;color:var(--white);letter-spacing:1px"><span style="width:12px;height:12px;background:var(--white)"></span>BRANKELL ADVISORY</div>
  <div class="abs" style="right:22px;top:170px;text-align:right;color:var(--white)">
    <div style="font:700 14px Montserrat,sans-serif">SECTION TITLE HERE</div>
    <div style="font:400 10px Lato,sans-serif;margin-top:2px">Subtext here</div>
  </div>
</section>

<section class="slide on-blue" style="left:382px;top:11px;background:var(--navy)">
  <div class="photo" role="img" aria-label="Blue-toned photo of a glass office tower" style="inset:0;background:linear-gradient(160deg,#0c4a9c,#1459b3 55%,#0a3f86)"></div>
  <h2 class="s-title white-title">SECTION TITLE HERE</h2>
  <div class="brand" style="color:var(--white)"><i style="background:var(--white)"></i>BRANKELL ADVISORY</div>
  <footer class="s-foot"><span>Copyright text here</span><span>Page: 01</span></footer>
</section>

<section class="slide" style="left:754px;top:11px">
  <h2 class="s-title">SECTION TITLE HERE</h2>
  <div class="brand"><i></i>BRANKELL ADVISORY</div>
  <footer class="s-foot"><span>Copyright text here</span><span>Page: 01</span></footer>
</section>

<section class="slide" style="left:1125px;top:11px">
  <h2 class="s-title">SECTION TITLE HERE</h2>
  <div class="brand"><i></i>BRANKELL ADVISORY</div>
  <div class="abs" style="left:12px;right:12px;top:47px">
    <h3 class="h mark">BULLET TITLE TEXT HERE</h3>
    <p class="p" style="padding-left:12px;margin-top:2px">Placeholder copy marks the spot where the client body text will go. Placeholder copy marks the spot where the client body text will go. Placeholder copy marks the spot where the client body text will go. Placeholder copy marks the spot where the client body text will go. Placeholder copy marks the spot where the client body text will go. Placeholder copy marks the spot where the client body text will go.</p>
  </div>
  <div class="abs" style="left:12px;right:12px;top:106px">
    <h3 class="h mark">BULLET TITLE TEXT HERE</h3>
    <p class="p" style="padding-left:12px;margin-top:2px">Placeholder copy marks the spot where the client body text will go. Placeholder copy marks the spot where the client body text will go. Placeholder copy marks the spot where the client body text will go. Placeholder copy marks the spot where the client body text will go. Placeholder copy marks the spot where the client body text will go. Placeholder copy marks the spot where the client body text will go.</p>
  </div>
  <div class="abs" style="left:12px;right:12px;top:164px">
    <h3 class="h mark">BULLET TITLE TEXT HERE</h3>
    <p class="p" style="padding-left:12px;margin-top:2px">Placeholder copy marks the spot where the client body text will go. Placeholder copy marks the spot where the client body text will go. Placeholder copy marks the spot where the client body text will go. Placeholder copy marks the spot where the client body text will go. Placeholder copy marks the spot where the client body text will go. Placeholder copy marks the spot where the client body text will go.</p>
  </div>
  <footer class="s-foot"><span>Copyright text here</span><span>Page: 01</span></footer>
</section>

<!-- Row 2 -->
<section class="slide" style="left:11px;top:278px">
  <h2 class="s-title">SECTION TITLE HERE</h2>
  <div class="brand"><i></i>BRANKELL ADVISORY</div>
  <div class="col4" style="left:0;background:var(--navy)">
    <svg width="38" height="38" viewBox="0 0 38 38" fill="none" stroke="#fff" stroke-width="1.4"><circle cx="19" cy="19" r="17"/><ellipse cx="19" cy="19" rx="7" ry="17"/><path d="M2 19h34M5 10h28M5 28h28M19 2v34"/></svg>
    <p class="p white">Placeholder copy marks the spot where the client body text will go. Placeholder copy marks the spot where the client body text will go. Placeholder copy marks the spot where the client body text will go. Placeholder copy marks the spot where the client body text will go.</p>
  </div>
  <div class="col4" style="left:91px;background:var(--blue)">
    <svg width="40" height="38" viewBox="0 0 40 38" fill="#fff"><circle cx="20" cy="5" r="3.5"/><circle cx="11" cy="9" r="3"/><circle cx="29" cy="9" r="3"/><circle cx="4" cy="17" r="3"/><circle cx="15" cy="17" r="3"/><circle cx="25" cy="17" r="3"/><circle cx="36" cy="17" r="3"/><rect x="1" y="22" width="6" height="14" rx="1"/><rect x="12" y="22" width="6" height="14" rx="1"/><rect x="22" y="22" width="6" height="14" rx="1"/><rect x="33" y="22" width="6" height="14" rx="1"/></svg>
    <p class="p white">Placeholder copy marks the spot where the client body text will go. Placeholder copy marks the spot where the client body text will go. Placeholder copy marks the spot where the client body text will go. Placeholder copy marks the spot where the client body text will go.</p>
  </div>
  <div class="col4" style="left:182px;background:var(--mid)">
    <svg width="38" height="38" viewBox="0 0 38 38" fill="none" stroke="#fff" stroke-width="1.4"><rect x="3" y="2" width="32" height="34"/><path d="M3 9h32"/><circle cx="7" cy="5.5" r="1"/><path d="M19 14v2M17 19h3v10h-3z"/></svg>
    <p class="p white">Placeholder copy marks the spot where the client body text will go. Placeholder copy marks the spot where the client body text will go. Placeholder copy marks the spot where the client body text will go. Placeholder copy marks the spot where the client body text will go.</p>
  </div>
  <div class="col4" style="left:273px;background:var(--sky)">
    <svg width="40" height="38" viewBox="0 0 40 38" fill="#fff"><circle cx="20" cy="5" r="3.5"/><circle cx="11" cy="9" r="3"/><circle cx="29" cy="9" r="3"/><circle cx="4" cy="17" r="3"/><circle cx="15" cy="17" r="3"/><circle cx="25" cy="17" r="3"/><circle cx="36" cy="17" r="3"/><rect x="1" y="22" width="6" height="14" rx="1"/><rect x="12" y="22" width="6" height="14" rx="1"/><rect x="22" y="22" width="6" height="14" rx="1"/><rect x="33" y="22" width="6" height="14" rx="1"/></svg>
    <p class="p white">Placeholder copy marks the spot where the client body text will go. Placeholder copy marks the spot where the client body text will go. Placeholder copy marks the spot where the client body text will go.</p>
  </div>
  <footer class="s-foot"><span>Copyright text here</span><span>Page: 01</span></footer>
</section>

<section class="slide" style="left:382px;top:278px">
  <h2 class="s-title">SECTION TITLE HERE</h2>
  <div class="brand"><i></i>BRANKELL ADVISORY</div>
  <div class="photo" role="img" aria-label="Black and white photo of a smiling business team" style="left:0;right:0;top:33px;height:97px;background:linear-gradient(90deg,#cfd2d6,#8e9297 40%,#c9ccd0 70%,#6e7277)"></div>
  <div class="abs" style="left:12px;width:160px;top:139px">
    <h3 class="h mark">PARAGRAPH TITLE HERE</h3>
    <p class="p" style="padding-left:9px;margin-top:3px">Placeholder copy marks the spot where the client body text will go. Placeholder copy marks the spot where the client body text will go. Placeholder copy marks the spot where the client body text will go. Placeholder copy marks the spot where the client body text will go.</p>
  </div>
  <div class="abs" style="left:190px;width:160px;top:139px">
    <h3 class="h mark">PARAGRAPH TITLE HERE</h3>
    <p class="p" style="padding-left:9px;margin-top:3px">Placeholder copy marks the spot where the client body text will go. Placeholder copy marks the spot where the client body text will go. Placeholder copy marks the spot where the client body text will go. Placeholder copy marks the spot where the client body text will go.</p>
  </div>
  <footer class="s-foot"><span>Copyright text here</span><span>Page: 01</span></footer>
</section>

<section class="slide" style="left:754px;top:278px">
  <h2 class="s-title">SECTION TITLE HERE</h2>
  <div class="brand"><i></i>BRANKELL ADVISORY</div>
  <div class="abs" style="left:10px;width:210px;top:46px">
    <h3 class="h mark">PARAGRAPH TITLE HERE</h3>
    <p class="p" style="padding-left:15px;margin-top:3px">Placeholder copy marks the spot where the client body text will go. Placeholder copy marks the spot where the client body text will go. Placeholder copy marks the spot where the client body text will go. Placeholder copy marks the spot where the client body text will go. Placeholder copy marks the spot where the client body text will go.</p>
    <p class="p" style="padding-left:15px;margin-top:9px">Placeholder copy marks the spot where the client body text will go. Placeholder copy marks the spot where the client body text will go. Placeholder copy marks the spot where the client body text will go.</p>
    <p class="p" style="padding-left:15px;margin-top:9px">Placeholder copy marks the spot where the client body text will go. Placeholder copy marks the spot where the client body text will go.</p>
  </div>
  <div class="photo" role="img" aria-label="Photo of a balance sheet with a pen and calculator" style="left:233px;right:0;top:52px;height:170px;background:linear-gradient(150deg,#d9dcdf,#f2f3f4 45%,#9da2a8 80%,#3d4147)"></div>
  <footer class="s-foot"><span>Copyright text here</span><span>Page: 01</span></footer>
</section>

<section class="slide" style="left:1125px;top:278px">
  <h2 class="s-title">SECTION TITLE HERE</h2>
  <div class="brand"><i></i>BRANKELL ADVISORY</div>
  <div class="abs" style="left:10px;width:160px;top:46px">
    <h3 class="h mark">PARAGRAPH TITLE HERE</h3>
    <p class="p" style="padding-left:15px;margin-top:3px">Placeholder copy marks the spot where the client body text will go. Placeholder copy marks the spot where the client body text will go. Placeholder copy marks the spot where the client body text will go. Placeholder copy marks the spot where the client body text will go. Placeholder copy marks the spot where the client body text will go. Placeholder copy marks the spot where the client body text will go. Placeholder copy marks the spot where the client body text will go. Placeholder copy marks the spot where the client body text will go.</p>
  </div>
  <div class="abs" style="left:188px;width:160px;top:46px">
    <h3 class="h mark">PARAGRAPH TITLE HERE</h3>
    <p class="p" style="padding-left:15px;margin-top:3px">Placeholder copy marks the spot where the client body text will go. Placeholder copy marks the spot where the client body text will go. Placeholder copy marks the spot where the client body text will go. Placeholder copy marks the spot where the client body text will go. Placeholder copy marks the spot where the client body text will go. Placeholder copy marks the spot where the client body text will go. Placeholder copy marks the spot where the client body text will go. Placeholder copy marks the spot where the client body text will go.</p>
  </div>
  <footer class="s-foot"><span>Copyright text here</span><span>Page: 01</span></footer>
</section>

<!-- Row 3 -->
<section class="slide" style="left:11px;top:544px">
  <h2 class="s-title">SECTION TITLE HERE</h2>
  <div class="brand"><i></i>BRANKELL ADVISORY</div>
  <div class="photo" role="img" aria-label="Photo of a pen on a balance sheet" style="left:14px;width:96px;top:36px;height:89px;background:linear-gradient(150deg,#e4e6e8,#b9bdc2 60%,#33373c)"></div>
  <div class="photo" role="img" aria-label="Photo of a pen on a balance sheet" style="left:134px;width:96px;top:36px;height:89px;background:linear-gradient(150deg,#e4e6e8,#b9bdc2 60%,#33373c)"></div>
  <div class="photo" role="img" aria-label="Photo of a pen on a balance sheet" style="left:254px;width:96px;top:36px;height:89px;background:linear-gradient(150deg,#e4e6e8,#b9bdc2 60%,#33373c)"></div>
  <div class="abs" style="left:14px;width:96px;top:132px"><h3 class="h" style="font-size:7.5px">IMAGE TITLE HERE</h3><p class="p" style="margin-top:2px">Placeholder copy marks the spot where the client body text will go. Placeholder copy marks the spot where the client body text will go. Placeholder copy marks the spot where the client body text will go. Placeholder copy marks the spot where the client body text will go.</p></div>
  <div class="abs" style="left:134px;width:96px;top:132px"><h3 class="h" style="font-size:7.5px">IMAGE TITLE HERE</h3><p class="p" style="margin-top:2px">Placeholder copy marks the spot where the client body text will go. Placeholder copy marks the spot where the client body text will go. Placeholder copy marks the spot where the client body text will go. Placeholder copy marks the spot where the client body text will go.</p></div>
  <div class="abs" style="left:254px;width:96px;top:132px"><h3 class="h" style="font-size:7.5px">IMAGE TITLE HERE</h3><p class="p" style="margin-top:2px">Placeholder copy marks the spot where the client body text will go. Placeholder copy marks the spot where the client body text will go. Placeholder copy marks the spot where the client body text will go. Placeholder copy marks the spot where the client body text will go.</p></div>
  <footer class="s-foot"><span>Copyright text here</span><span>Page: 01</span></footer>
</section>

<section class="slide" style="left:382px;top:544px">
  <h2 class="s-title">SECTION TITLE HERE</h2>
  <div class="brand"><i></i>BRANKELL ADVISORY</div>
  <div class="photo" role="img" aria-label="Photo of a balance sheet with a calculator and pen" style="left:0;width:170px;top:27px;height:211px;background:linear-gradient(150deg,#d7dadd,#f0f1f2 40%,#a3a8ae 75%,#2e3237)"></div>
  <div class="abs" style="left:0;top:38px;width:130px;height:18px;background:var(--navy);color:var(--white);font:700 9px/18px Montserrat,sans-serif;padding-left:4px;box-sizing:border-box">INFASTRUCTURE</div>
  <div class="abs" style="left:170px;right:0;top:27px;height:211px;background:var(--navy);padding:14px 14px 0;box-sizing:border-box">
    <p class="p white">Placeholder copy marks the spot where the client body text will go. Placeholder copy marks the spot where the client body text will go. Placeholder copy marks the spot where the client body text will go. Placeholder copy marks the spot where the client body text will go. Placeholder copy marks the spot where the client body text will go.</p>
    <p class="p white" style="margin-top:8px">Placeholder copy marks the spot where the client body text will go. Placeholder copy marks the spot where the client body text will go. Placeholder copy marks the spot where the client body text will go. Placeholder copy marks the spot where the client body text will go. Placeholder copy marks the spot where the client body text will go.</p>
    <p class="p white" style="margin-top:8px">Placeholder copy marks the spot where the client body text will go. Placeholder copy marks the spot where the client body text will go.</p>
  </div>
  <footer class="s-foot"><span>Copyright text here</span><span>Page: 01</span></footer>
</section>

<section class="slide" style="left:754px;top:544px">
  <h2 class="s-title">SECTION TITLE HERE</h2>
  <div class="brand"><i></i>BRANKELL ADVISORY</div>
  <div class="photo" role="img" aria-label="Faint photo of a glass office building" style="left:0;right:0;top:27px;height:114px;background:linear-gradient(100deg,#d9dde2,#f3f4f6 55%,#eef0f2)"></div>
  <div class="abs" style="left:200px;width:150px;top:58px">
    <h3 style="margin:0;font:500 12px Montserrat,sans-serif;color:var(--blue)">IMAGE TITLE HERE</h3>
    <p class="p" style="margin-top:4px;color:#b5b9c0">Placeholder copy marks the spot where the client body text will go. Placeholder copy marks the spot where the client body text will go. Placeholder copy marks the spot where the client body text will go.</p>
  </div>
  <div class="abs" style="left:0;right:0;top:141px;height:97px;background:var(--blue);padding:8px 10px 0;box-sizing:border-box">
    <h3 style="margin:0 0 5px;font:500 10px Montserrat,sans-serif;color:var(--white)">OUT KICKOFF MEETING</h3>
    <p class="p white">Placeholder copy marks the spot where the client body text will go. Placeholder copy marks the spot where the client body text will go. Placeholder copy marks the spot where the client body text will go. Placeholder copy marks the spot where the client body text will go. Placeholder copy marks the spot where the client body text will go. Placeholder copy marks the spot where the client body text will go. Placeholder copy marks the spot where the client body text will go. Placeholder copy marks the spot where the client body text will go.</p>
  </div>
  <footer class="s-foot"><span>Copyright text here</span><span>Page: 01</span></footer>
</section>

<section class="slide" style="left:1125px;top:544px">
  <h2 class="s-title">SECTION TITLE HERE</h2>
  <div class="brand"><i></i>BRANKELL ADVISORY</div>
  <p class="p abs" style="left:14px;right:10px;top:34px">Placeholder copy marks the spot where the client body text will go. Placeholder copy marks the spot where the client body text will go. Placeholder copy marks the spot where the client body text will go. Placeholder copy marks the spot where the client body text will go. Placeholder copy marks the spot where the client body text will go.</p>
  <div class="abs" style="left:11px;width:342px;top:89px;height:15px;background:var(--navy);color:var(--white);font:600 5.5px/15px Montserrat,sans-serif"><span style="margin-left:16px">SECTION</span><span style="margin-left:30px">MAIN TITLE HERE</span></div>
  <div class="tbl-row" style="top:109px;background:#eceff3"><b>ICON - 1</b><p class="p">Placeholder copy marks the spot where the client body text will go. Placeholder copy marks the spot where the client body text will go.</p></div>
  <div class="tbl-row" style="top:133px"><b>ICON - 1</b><p class="p">Placeholder copy marks the spot where the client body text will go. Placeholder copy marks the spot where the client body text will go.</p></div>
  <div class="tbl-row" style="top:156px;background:#eceff3"><b>ICON - 1</b><p class="p">Placeholder copy marks the spot where the client body text will go. Placeholder copy marks the spot where the client body text will go.</p></div>
  <div class="tbl-row" style="top:180px"><b>ICON - 1</b><p class="p">Placeholder copy marks the spot where the client body text will go. Placeholder copy marks the spot where the client body text will go.</p></div>
  <div class="tbl-row" style="top:204px;background:#eceff3"><b>ICON - 1</b><p class="p">Placeholder copy marks the spot where the client body text will go. Placeholder copy marks the spot where the client body text will go.</p></div>
  <footer class="s-foot"><span>Copyright text here</span><span>Page: 01</span></footer>
</section>

<!-- Row 4 -->
<section class="slide on-blue" style="left:11px;top:811px;background:var(--navy)">
  <div class="photo" role="img" aria-label="Blue-toned photo of a business person" style="inset:0;background:linear-gradient(120deg,#0f57b0,#1764c2 50%,#0c4795)"></div>
  <div class="abs" style="left:0;right:0;top:98px;display:flex;justify-content:center;align-items:center;gap:6px;font:600 17px Montserrat,sans-serif;color:var(--white);letter-spacing:1px"><span style="width:14px;height:14px;background:var(--white)"></span>BRANKELL ADVISORY</div>
  <div class="abs" style="left:0;right:0;top:143px;text-align:center;color:var(--white)">
    <div style="font:500 10.5px Montserrat,sans-serif">THANKS FOR YOUR VALUABLE TIMES</div>
    <div style="font:400 7px/12px Lato,sans-serif;margin-top:6px">Contact Details Here<br>Contact Details Here<br>Contact Details Here</div>
  </div>
  <footer class="s-foot"><span>Copyright text here</span><span>Page: 01</span></footer>
</section>

<section class="slide" style="left:382px;top:811px">
  <h2 class="s-title">SECTION TITLE HERE</h2>
  <div class="brand"><i></i>BRANKELL ADVISORY</div>
  <svg class="abs" style="left:0;top:0" width="364" height="257" viewBox="0 0 364 257">
    <defs><linearGradient id="wave" x1="0" y1="0" x2="0" y2="1"><stop offset="0" stop-color="#1660c0"/><stop offset="1" stop-color="#2c86e2"/></linearGradient></defs>
    <g class="axis" text-anchor="middle"><text x="16" y="66">60</text><text x="16" y="89">50</text><text x="16" y="112">40</text><text x="16" y="136">30</text><text x="16" y="159">20</text><text x="16" y="183">10</text><text x="26" y="212">Jan</text><text x="104" y="212">Feb</text><text x="183" y="212">Mar</text><text x="262" y="212">Apr</text><text x="340" y="212">May</text></g>
    <path d="M25,204 L25,150 C35,120 45,95 55,100 C65,105 70,135 80,135 C92,135 95,110 108,110 C122,110 125,140 140,140 C152,140 158,75 172,75 C185,75 185,140 198,140 C210,140 212,95 222,95 C232,95 235,140 245,130 C255,120 255,63 264,63 C274,63 275,120 285,120 C295,120 300,95 310,95 C320,95 322,140 330,132 L338,120 L338,204 Z" fill="url(#wave)"/>
    <g stroke="#fff" stroke-opacity=".25" stroke-width=".6"><path d="M25,158H338M25,181H338"/></g>
    <circle cx="264" cy="63" r="3" fill="#fff" stroke="#2d3540" stroke-width="1"/>
    <text x="264" y="54" text-anchor="middle" style="font:700 6.5px Montserrat,sans-serif;fill:#2d3540">YOUR TEXT</text>
  </svg>
  <footer class="s-foot"><span>Copyright text here</span><span>Page: 01</span></footer>
</section>

<section class="slide" style="left:754px;top:811px">
  <h2 class="s-title">SECTION TITLE HERE</h2>
  <div class="brand"><i></i>BRANKELL ADVISORY</div>
  <svg class="abs" style="left:0;top:0" width="364" height="257" viewBox="0 0 364 257">
    <g class="axis"><text x="16" y="56">100</text><text x="16" y="72">90</text><text x="16" y="88">80</text><text x="16" y="104">70</text><text x="16" y="120">60</text><text x="16" y="136">50</text><text x="16" y="152">40</text><text x="16" y="168">30</text><text x="16" y="184">20</text><text x="16" y="200">10</text></g>
    <g class="axis" text-anchor="middle"><text x="50" y="217">100</text><text x="109" y="217">200</text><text x="167" y="217">300</text><text x="225" y="217">400</text><text x="283" y="217">500</text><text x="341" y="217">600</text></g>
    <path d="M40,204 L40,185 L70,165 L100,140 L120,150 L155,100 L175,125 L205,70 L235,90 L260,95 L285,115 L300,120 L318,110 L340,125 L348,150 L348,204 Z" fill="#1d72d2"/>
  </svg>
  <footer class="s-foot"><span>Copyright text here</span><span>Page: 01</span></footer>
</section>

<section class="slide" style="left:1125px;top:811px">
  <h2 class="s-title">SECTION TITLE HERE</h2>
  <div class="brand"><i></i>BRANKELL ADVISORY</div>
  <svg class="abs" style="left:0;top:0" width="364" height="257" viewBox="0 0 364 257">
    <path d="M175,38V225" stroke="#c5cbd3" stroke-width="1"/>
    <g fill="#fff" stroke="#1660c0" stroke-width="1.2"><circle cx="175" cy="57" r="17"/><circle cx="175" cy="107" r="17"/><circle cx="175" cy="156" r="17"/><circle cx="175" cy="205" r="17"/></g>
    <g fill="#1660c0"><circle cx="175" cy="57" r="14"/><circle cx="175" cy="107" r="14"/><circle cx="175" cy="156" r="14"/><circle cx="175" cy="205" r="14"/></g>
    <g fill="none" stroke="#fff" stroke-width="1.3"><circle cx="174" cy="56" r="5"/><path d="M178,60l4,4"/><rect x="168" y="101" width="13" height="12" rx="2"/><path d="M171,105h7M171,109h5"/><path d="M168,158a5,5 0 0 1 3-7a6,6 0 0 1 11,2a3,3 0 0 1 0,6h-12z"/><rect x="168" y="199" width="14" height="11"/><path d="M172,203h6"/></g>
    <g stroke="#1660c0" stroke-width="1"><path d="M208,71H262M92,121H148M208,170H262M92,219H148"/></g>
    <text x="167" y="37" style="font:400 5px Lato,sans-serif;fill:#8b9099">Start</text>
    <text x="168" y="232" style="font:400 5px Lato,sans-serif;fill:#8b9099">Finish</text>
  </svg>
  <div class="abs big-year" style="left:208px;top:56px">2016</div>
  <div class="abs big-year" style="left:118px;top:105px">2017</div>
  <div class="abs big-year" style="left:208px;top:155px">2018</div>
  <div class="abs big-year" style="left:118px;top:203px">2019</div>
  <div class="abs" style="left:77px;top:37px;width:70px"><div class="pct">23%</div><div class="pct" style="font-weight:600">Lorem ipsum</div><p class="p" style="font-size:3.8px;line-height:5px">Placeholder copy marks the spot where the client body text will go.</p></div>
  <div class="abs" style="left:217px;top:88px;width:70px"><div class="pct">32%</div><div class="pct" style="font-weight:600">Quasi beatae</div><p class="p" style="font-size:3.8px;line-height:5px">Placeholder copy marks the spot where the client body text will go.</p></div>
  <div class="abs" style="left:77px;top:136px;width:70px"><div class="pct">45%</div><div class="pct" style="font-weight:600">Vitae dicta</div><p class="p" style="font-size:3.8px;line-height:5px">Placeholder copy marks the spot where the client body text will go.</p></div>
  <div class="abs" style="left:217px;top:185px;width:70px"><div class="pct">59%</div><div class="pct" style="font-weight:600">Omnis iste</div><p class="p" style="font-size:3.8px;line-height:5px">Placeholder copy marks the spot where the client body text will go.</p></div>
  <footer class="s-foot"><span>Copyright text here</span><span>Page: 01</span></footer>
</section>

<!-- Row 5 -->
<section class="slide" style="left:11px;top:1078px">
  <h2 class="s-title">SECTION TITLE HERE</h2>
  <div class="brand"><i></i>BRANKELL ADVISORY</div>
  <svg class="abs" style="left:0;top:0" width="364" height="257" viewBox="0 0 364 257">
    <g style="font:400 5.5px Lato,sans-serif;fill:#2d3540"><text x="8" y="57">Add your text &amp; data</text><text x="8" y="79">Add your text &amp; data</text><text x="8" y="100">Add your text &amp; data</text><text x="8" y="122">Add your text &amp; data</text><text x="8" y="144">Add your text &amp; data</text><text x="8" y="166">Add your text &amp; data</text><text x="8" y="187">Add your text &amp; data</text><text x="8" y="209">Add your text &amp; data</text></g>
    <g fill="#e1e5eb"><rect x="100" y="53" width="255" height="5"/><rect x="100" y="75" width="255" height="5"/><rect x="100" y="96" width="255" height="5"/><rect x="100" y="118" width="255" height="5"/><rect x="100" y="140" width="255" height="5"/><rect x="100" y="162" width="255" height="5"/><rect x="100" y="183" width="255" height="5"/><rect x="100" y="205" width="255" height="5"/></g>
    <g fill="#1660c0"><rect x="195" y="53" width="60" height="5"/><rect x="248" y="75" width="60" height="5"/><rect x="125" y="96" width="60" height="5"/><rect x="175" y="118" width="60" height="5"/><rect x="243" y="140" width="60" height="5"/><rect x="277" y="162" width="60" height="5"/><rect x="195" y="183" width="60" height="5"/><rect x="134" y="205" width="60" height="5"/></g>
    <g style="font:700 6px Montserrat,sans-serif;fill:#2d3540" text-anchor="middle"><text x="225" y="50">49%</text><text x="278" y="72">63%</text><text x="155" y="93">23%</text><text x="205" y="115">38%</text><text x="273" y="137">57%</text><text x="307" y="159">71%</text><text x="225" y="180">44%</text><text x="164" y="202">29%</text></g>
  </svg>
  <footer class="s-foot"><span>Copyright text here</span><span>Page: 01</span></footer>
</section>

<section class="slide" style="left:382px;top:1078px">
  <h2 class="s-title">SECTION TITLE HERE</h2>
  <div class="brand"><i></i>BRANKELL ADVISORY</div>
  <svg class="abs" style="left:0;top:0" width="364" height="257" viewBox="0 0 364 257">
    <g fill="#fff" stroke="#8b9099" stroke-width=".7"><circle cx="28" cy="60" r="9"/><circle cx="28" cy="87" r="9"/><circle cx="28" cy="115" r="9"/><circle cx="28" cy="143" r="9"/><circle cx="28" cy="171" r="9"/><circle cx="28" cy="198" r="9"/></g>
    <g style="font:400 4.5px Lato,sans-serif;fill:#5a606a" text-anchor="middle"><text x="28" y="62">Jun</text><text x="28" y="89">May</text><text x="28" y="117">Apr</text><text x="28" y="145">Mar</text><text x="28" y="173">Feb</text><text x="28" y="200">Jan</text></g>
    <g><rect x="58" y="55" width="230" height="10" rx="5" fill="#5aa8f0"/><rect x="58" y="82" width="175" height="10" rx="5" fill="#3f95e8"/><rect x="58" y="110" width="160" height="10" rx="5" fill="#2c86e2"/><rect x="58" y="138" width="144" height="10" rx="5" fill="#1d72d2"/><rect x="58" y="166" width="118" height="10" rx="5" fill="#1a68c8"/><rect x="58" y="193" width="100" height="10" rx="5" fill="#1660c0"/></g>
    <g style="font:700 5px Montserrat,sans-serif;fill:#2d3540"><text x="294" y="62">3,003,690</text><text x="239" y="89">2,690,456</text><text x="224" y="117">2,133,456</text><text x="208" y="145">1,890,098</text><text x="182" y="173">1,456,146</text><text x="164" y="200">1,233,456</text></g>
    <g class="axis" text-anchor="middle" style="font-size:5px"><text x="30" y="224">0</text><text x="76" y="224">100</text><text x="126" y="224">500</text><text x="176" y="224">1000</text><text x="226" y="224">1500</text><text x="278" y="224">2000</text><text x="330" y="224">2500</text></g>
  </svg>
  <footer class="s-foot"><span>Copyright text here</span><span>Page: 01</span></footer>
</section>

<section class="slide" style="left:754px;top:1078px">
  <h2 class="s-title">SECTION TITLE HERE</h2>
  <div class="brand"><i></i>BRANKELL ADVISORY</div>
  <svg class="abs" style="left:0;top:0" width="364" height="257" viewBox="0 0 364 257">
    <g fill="none" stroke="#1660c0" stroke-width="1.4"><circle cx="74" cy="103" r="45" stroke-dasharray="249 34" transform="rotate(55 74 103)"/><circle cx="186" cy="103" r="45" stroke-dasharray="249 34" transform="rotate(55 186 103)"/><circle cx="298" cy="103" r="45" stroke-dasharray="249 34" transform="rotate(55 298 103)"/></g>
    <g style="font:600 15px Montserrat,sans-serif;fill:#5a606a" text-anchor="middle"><text x="74" y="109">88%</text><text x="186" y="109">88%</text><text x="298" y="109">88%</text></g>
    <g style="font:700 10px Montserrat,sans-serif;fill:#1660c0" text-anchor="middle"><text x="74" y="174">ADD TEXT</text><text x="186" y="174">ADD TEXT</text><text x="298" y="174">ADD TEXT</text></g>
  </svg>
  <p class="p abs" style="left:28px;width:92px;top:179px;text-align:center;color:#5a606a">Placeholder copy marks the spot where the client body text will go.</p>
  <p class="p abs" style="left:140px;width:92px;top:179px;text-align:center;color:#5a606a">Placeholder copy marks the spot where the client body text will go.</p>
  <p class="p abs" style="left:252px;width:92px;top:179px;text-align:center;color:#5a606a">Placeholder copy marks the spot where the client body text will go.</p>
  <footer class="s-foot"><span>Copyright text here</span><span>Page: 01</span></footer>
</section>

<section class="slide" style="left:1125px;top:1078px">
  <h2 class="s-title">SECTION TITLE HERE</h2>
  <div class="brand"><i></i>BRANKELL ADVISORY</div>
  <svg class="abs" style="left:0;top:0" width="364" height="257" viewBox="0 0 364 257">
    <path d="M30,88H335" stroke="#1660c0" stroke-width="1"/>
    <g fill="#1660c0"><circle cx="30" cy="88" r="2.5"/><circle cx="335" cy="88" r="2.5"/></g>
    <g fill="#fff" stroke="#1660c0" stroke-width="1"><circle cx="67" cy="88" r="34"/><circle cx="145" cy="88" r="34"/><circle cx="221" cy="88" r="34"/><circle cx="300" cy="88" r="34"/></g>
    <g fill="#1660c0"><circle cx="67" cy="88" r="28"/><circle cx="145" cy="88" r="28"/><circle cx="221" cy="88" r="28"/><circle cx="300" cy="88" r="28"/></g>
    <g fill="none" stroke="#fff" stroke-width="1.5"><circle cx="64" cy="85" r="9"/><path d="M55,85h18M64,76v18M71,92l7,7"/><rect x="136" y="76" width="18" height="12" rx="2"/><path d="M140,82h10M138,92h8v8h-8z"/><path d="M210,94a6,6 0 0 1 3-9a8,8 0 0 1 15,2a4,4 0 0 1 0,8h-18z"/><rect x="290" y="78" width="20" height="18"/><path d="M300,82l2,5h5l-4,3l2,5l-5-3l-5,3l2-5l-4-3h5z"/></g>
  </svg>
  <div class="abs" style="left:30px;width:74px;top:143px;text-align:center"><h3 class="h" style="font-size:6.5px">ICON TITLE HERE</h3><p class="p" style="font-size:6.5px;line-height:8.2px;color:#5a606a;margin-top:2px">Placeholder copy marks the spot where the client body text will go.</p></div>
  <div class="abs" style="left:108px;width:74px;top:143px;text-align:center"><h3 class="h" style="font-size:6.5px">ICON TITLE HERE</h3><p class="p" style="font-size:6.5px;line-height:8.2px;color:#5a606a;margin-top:2px">Placeholder copy marks the spot where the client body text will go.</p></div>
  <div class="abs" style="left:184px;width:74px;top:143px;text-align:center"><h3 class="h" style="font-size:6.5px">ICON TITLE HERE</h3><p class="p" style="font-size:6.5px;line-height:8.2px;color:#5a606a;margin-top:2px">Placeholder copy marks the spot where the client body text will go.</p></div>
  <div class="abs" style="left:263px;width:74px;top:143px;text-align:center"><h3 class="h" style="font-size:6.5px">ICON TITLE HERE</h3><p class="p" style="font-size:6.5px;line-height:8.2px;color:#5a606a;margin-top:2px">Placeholder copy marks the spot where the client body text will go.</p></div>
  <footer class="s-foot"><span>Copyright text here</span><span>Page: 01</span></footer>
</section>

</main>
</body>
</html>
```